Wine Tasting Event

We need a flyer design for a wine tasting event on Friday, February 14th. This is NOT a Valentine's themed event. It's merely an event for both singles and couples who do not want to drop a ton of money on a traditional meal at a fine restaurant. There will be good wines to taste, light snacks, info sessions on how to taste/appreciate good wine, live music, and a full bar in addition to the wine.

The event is called "Poured by the Greenway" and will be held at a venue overlooking the beautiful Marrow Creek Trail path.

We had an initial idea of a Large Wine cork taking up the majority of the flyer, with all of the information printed on it (as if it were a part of the cork). We are not designers, but have attached the initial attempt at the idea. Warning - It's bad.

Target Market(s)

Men and Women aged 21-35.

Industry/Entity Type

Restaurant

Requirements
Must have
• Name: Poured by the Greenway
Date: Friday, February 14th
Logo: Dunmore Leisure and Games League (See Attached File)

*NOTE Logo should not be a focal point of design. Just needs to be somewhere on the flyer. Can be substituted fo "Dunmore Leisure and Games League Presents"

Needs to be adaptable for 4"x6", 8.5"x11", and 11"x17"
Nice to have
• Wine cork, bottle, or glass. Something Atlanta related, or related to the Marrow Creek Trail.
Should not have
• Anything related to Valentine's Day

```html
<!DOCTYPE html>
<html lang="en">
<head>
<meta charset="utf-8">
<title>Poured by the Greenway – Wine Tasting Event</title>
<link href="https://fonts.googleapis.com/css2?family=Black+Ops+One&family=Lobster&family=Arimo:ital,wght@0,700;1,700&display=swap" rel="stylesheet">
<style>
  :root {
    --green-deep: #0f8a3c;
    --green-teal: #2fbf86;
    --green-bright: #4fe02a;
    --green-badge: #5ad33a;
    --mist: #f4fbf5;
    --ink: #111111;
    --red: #e0101a;
    --white: #ffffff;
    --gold-dark: #8a7636;
    --gold-mid: #cbb46a;
    --cream: #efe6c8;
  }
  html, body {
    margin: 0;
    padding: 0;
    width: 927px;
    height: 1200px;
    overflow: hidden;
    background: var(--white);
  }
  .flyer {
    position: relative;
    width: 927px;
    height: 1200px;
    overflow: hidden;
    font-family: "Arimo", Arial, sans-serif;
    background:
      radial-gradient(ellipse 420px 380px at 600px 660px, var(--mist) 0%, rgba(244,251,245,0.85) 45%, rgba(244,251,245,0) 100%),
      radial-gradient(ellipse 520px 520px at 880px 1100px, var(--green-bright) 0%, rgba(79,224,42,0) 80%),
      linear-gradient(160deg, var(--green-teal) 0%, #6fd9a4 30%, #dff5e6 55%, #9be86f 78%, var(--green-deep) 100%);
  }
  .bottle-photo {
    position: absolute;
    left: 0;
    top: 220px;
    width: 660px;
    height: 980px;
    background:
      radial-gradient(ellipse 210px 260px at 440px 230px, rgba(239,230,200,0.95) 0%, rgba(239,230,200,0.7) 45%, rgba(239,230,200,0) 100%),
      radial-gradient(ellipse 420px 620px at 170px 820px, rgba(203,180,106,0.95) 0%, rgba(138,118,54,0.75) 55%, rgba(138,118,54,0) 100%);
  }
  .title-main {
    position: absolute;
    left: 40px;
    top: 50px;
    width: 840px;
    margin: 0;
    text-align: center;
    font-family: "Black Ops One", "Arial Black", sans-serif;
    font-weight: 400;
    font-size: 165px;
    line-height: 1;
    letter-spacing: 6px;
    color: var(--ink);
    transform: rotate(-8deg);
    text-shadow: 3px 3px 0 var(--white), -3px -3px 0 var(--white), 3px -3px 0 var(--white), -3px 3px 0 var(--white);
  }
  .title-script {
    position: absolute;
    left: 285px;
    top: 300px;
    margin: 0;
    font-family: "Lobster", cursive;
    font-weight: 400;
    font-size: 80px;
    line-height: 1;
    color: var(--red);
    transform: rotate(-22deg);
    transform-origin: left center;
    -webkit-text-stroke: 2px var(--ink);
    paint-order: stroke fill;
    text-shadow: 4px 0 0 var(--white), -4px 0 0 var(--white), 0 4px 0 var(--white), 0 -4px 0 var(--white), 3px 3px 0 var(--white), -3px -3px 0 var(--white);
  }
  .join-badge {
    position: absolute;
    left: 596px;
    top: 383px;
    width: 208px;
    height: 208px;
  }
  .event-heading {
    position: absolute;
    left: 90px;
    top: 622px;
    width: 800px;
    margin: 0;
    text-align: center;
    font-style: italic;
    font-weight: 700;
    font-size: 63px;
    line-height: 80px;
    letter-spacing: -1.5px;
    color: var(--red);
    -webkit-text-stroke: 2px var(--ink);
    paint-order: stroke fill;
    text-shadow: 3px 0 0 var(--white), -3px 0 0 var(--white), 0 3px 0 var(--white), 0 -3px 0 var(--white), 3px 3px 0 var(--white), -3px -3px 0 var(--white), 3px -3px 0 var(--white), -3px 3px 0 var(--white);
  }
  .presenter {
    position: absolute;
    left: 390px;
    top: 875px;
    width: 340px;
    display: flex;
    align-items: center;
    justify-content: center;
    gap: 10px;
  }
  .presenter-dot {
    flex: 0 0 auto;
    width: 22px;
    height: 22px;
    border-radius: 50%;
    background: var(--red);
  }
  .presenter-name {
    margin: 0;
    font-weight: 700;
    font-size: 24px;
    line-height: 1.2;
    color: var(--ink);
  }
  .event-details {
    position: absolute;
    left: 248px;
    top: 955px;
    width: 640px;
    margin: 0;
    text-align: center;
    font-style: italic;
    font-weight: 700;
    font-size: 27px;
    line-height: 37px;
    color: var(--ink);
    text-shadow: 2px 0 0 var(--white), -2px 0 0 var(--white), 0 2px 0 var(--white), 0 -2px 0 var(--white), 2px 2px 0 var(--white), -2px -2px 0 var(--white);
  }
  .join-line {
    position: absolute;
    left: 213px;
    top: 1122px;
    width: 665px;
    display: flex;
    align-items: flex-end;
    gap: 6px;
    font-size: 32px;
    color: var(--white);
  }
  .join-line span { white-space: nowrap; }
  .join-line .fill-rule {
    flex: 1;
    border-bottom: 2px solid var(--white);
    height: 30px;
  }
</style>
</head>
<body>
<main class="flyer">
  <div class="bottle-photo" role="img" aria-label="Photograph of a gold-foiled sparkling wine bottle rising from the lower left, its cork bursting upward in a spray of wine and bubbles"></div>

  <h1 class="title-main">POURED</h1>
  <p class="title-script">by the Greenway</p>

  <svg class="join-badge" viewBox="0 0 208 208" aria-label="Join now">
    <circle cx="104" cy="104" r="100" fill="var(--white)" stroke="var(--ink)" stroke-width="3"/>
    <circle cx="104" cy="104" r="86" fill="none" stroke="var(--green-badge)" stroke-width="14"/>
    <circle cx="104" cy="104" r="78" fill="none" stroke="var(--ink)" stroke-width="2"/>
    <g transform="rotate(28 104 104)" font-family="Arimo, Arial, sans-serif" font-weight="700" font-size="46" text-anchor="middle" fill="var(--green-badge)" stroke="var(--ink)" stroke-width="2" paint-order="stroke fill">
      <text x="104" y="98">JOIN</text>
      <text x="104" y="146">NOW</text>
    </g>
  </svg>

  <h2 class="event-heading">Wine Tasting Event<br>on Friday, February 14th</h2>

  <div class="presenter">
    <span class="presenter-dot"></span>
    <p class="presenter-name">Dunmore Leisure and Games League</p>
  </div>

  <p class="event-details">There will be good wines to taste, light snacks, info sessions on how to taste/appreciate good wine, live music, and a full bar in addition to the wine.</p>

  <div class="join-line"><span>Join Us :</span><span class="fill-rule"></span></div>
</main>
</body>
</html>
```